Corporate Powerpoint Presentation Template

Ta Merosk Technology Consulting Group is looking to have a comprehensive Powerpoint Template designed. The template must contain a wide selection for slide templates that can be used for proposals, project reporting and general marketing purposes, including graphs, infographics etc.. Please review supporting documentation attached.

```html
<!DOCTYPE html>
<html lang="en">
<head>
<meta charset="utf-8">
<title>Ta Merosk — Presentation Template Overview</title>
<link href="https://fonts.googleapis.com/css2?family=Poppins:wght@400;500;600;700&display=swap" rel="stylesheet">
<style>
:root{
  --navy:#1f1aa0;
  --navy-deep:#16127a;
  --gold:#c9a95c;
  --gold-soft:#e6d4a6;
  --paper:#f4f4f4;
  --card:#ffffff;
  --ink:#1b1a4f;
  --muted:#8a8a99;
  --line:#dedee6;
  --backdrop:#d8d8d5;
}
*{box-sizing:border-box;margin:0;padding:0}
html,body{width:1200px;height:996px;overflow:hidden;background:var(--backdrop);font-family:"Poppins",sans-serif;color:var(--ink)}
.deck{position:relative;width:1200px;height:996px}
.slide{position:absolute;width:227px;height:127px;background:var(--paper);overflow:hidden;box-shadow:0 1px 3px rgba(0,0,0,.12)}
.slide.navy{background:var(--navy);color:#fff}
.slide.white{background:#fff}
.ab{position:absolute}
.title{font-weight:600;color:var(--ink);line-height:1.1}
.gold{color:var(--gold)}
.tiny{font-size:2.6px;line-height:1.35;color:var(--muted)}
.small{font-size:3.2px;line-height:1.35;color:var(--ink)}
.foot{position:absolute;left:7px;bottom:5px;font-size:2.6px;color:var(--muted)}
.foot b{color:var(--navy);font-weight:600;margin-right:2px}
.num{position:absolute;right:7px;bottom:5px;font-size:3px;color:var(--ink)}
.photo{position:absolute}
.photo-blue{background:linear-gradient(135deg,#2d3ca8,#5a79c9 55%,#8fa7dc)}
.photo-office{background:linear-gradient(135deg,#9b8d80,#cfc6bb 50%,#6d6156)}
.photo-violet{background:linear-gradient(135deg,#4b44a8,#8f86c8 60%,#b7b1de)}
.photo-city{background:linear-gradient(180deg,#a8c4e0,#d7e3ee 55%,#c9ccd2)}
.card{position:absolute;background:var(--card);border-radius:2px;box-shadow:0 0 2px rgba(0,0,0,.08)}
.btn{position:absolute;font-size:2.6px;padding:1px 4px;border-radius:4px}
.avatar{position:absolute;border-radius:50%;background:linear-gradient(160deg,#d9c3a8,#9c8470)}
.avatar.ring{border:1.5px solid #fff}
.tick{display:inline-block;width:3px;height:3px;border-radius:50%;border:.5px solid var(--gold);margin-right:2px;vertical-align:middle}
.tabs{position:absolute;left:14px;right:14px;top:6px;height:9px;background:#fff;border-radius:2px;display:flex;justify-content:space-around;align-items:center;font-size:2.3px;color:var(--ink)}
.nav{position:absolute;display:flex;gap:6px;font-size:2.4px;color:#fff;white-space:nowrap}
.tbl{position:absolute;border-collapse:collapse;font-size:2.2px;color:var(--ink)}
.tbl th{background:var(--navy);color:#fff;font-weight:500;padding:.8px 1px}
.tbl th.g{background:var(--gold)}
.tbl td{padding:.8px 1px;border-bottom:.3px solid var(--line);text-align:center}
.tbl td:first-child{text-align:left;font-weight:500}
.tbl tr.total td{background:var(--gold);color:#fff;font-weight:600;border:0}
.tbl tr.navyrow td{background:var(--navy);color:#fff;border:0}
.plan{position:absolute;top:24px;width:46px;height:86px;background:#fff;border-radius:2px}
.plan .head{height:28px;padding:4px;color:#fff;font-size:2.8px}
.plan .head b{display:block;font-size:8px;font-weight:600;margin-top:2px}
.plan ul{list-style:none;padding:3px 4px;font-size:2.2px;line-height:1.5;color:var(--muted)}
.plan .more{position:absolute;left:4px;right:4px;bottom:5px;height:7px;border-radius:1px;font-size:2.2px;color:#fff;text-align:center;line-height:7px}
.person{position:absolute;text-align:center;font-size:2.8px;width:36px}
.person .name{font-weight:600;margin-top:1px}
.person .role{font-size:2.2px;opacity:.8}
.bubble{position:absolute;border-radius:50%;display:flex;align-items:center;justify-content:center;text-align:center;font-size:2.6px;line-height:1.1}
.calendar{position:absolute;display:grid;grid-template-columns:repeat(7,6px);row-gap:1.6px;font-size:2.2px;color:var(--ink);text-align:center}
.calendar .dow{font-weight:600}
.calendar .on{color:var(--navy);font-weight:600}
.firm-name{font-size:10px;font-weight:500;color:var(--navy-deep)}
</style>
</head>
<body>
<main class="deck">

<!-- Row 1 -->
<section class="slide navy" style="left:28.6px;top:29.7px">
  <svg class="ab" width="227" height="127" viewBox="0 0 227 127" role="img" aria-label="City skyline and handshake photo in diagonal frame">
    <defs><linearGradient id="ph1" x1="0" y1="0" x2="1" y2="1"><stop offset="0" stop-color="#7a86c4"/><stop offset="1" stop-color="#c9cfe6"/></linearGradient></defs>
    <polygon points="0,38 62,0 106,0 40,127 0,127" fill="url(#ph1)"/>
    <polygon points="110,0 132,0 64,127 42,127" fill="var(--gold)"/>
  </svg>
  <div class="ab" style="left:20px;top:14px;font-size:12px;font-weight:600">TM</div>
  <div class="ab title" style="left:122px;top:46px;font-size:12px;color:#fff">Introduction to<br>Ta Merosk</div>
  <div class="ab tiny" style="left:124px;top:76px;color:#dcdcf0;width:95px">Empowering Enterprises to Innovate through Intelligent Architecture, Automation &amp; AI</div>
  <div class="btn" style="left:168px;top:98px;background:var(--gold);color:#fff">More Info ›</div>
  <div class="btn" style="left:190px;top:98px;border:.4px solid #fff;color:#fff">See More ›</div>
</section>

<section class="slide navy" style="left:258.9px;top:29.7px">
  <div class="photo photo-violet" role="img" aria-label="Handshake photo tinted in blue" style="left:80px;top:0;width:92px;height:127px;opacity:.35"></div>
  <div class="ab" style="left:167px;top:0;width:60px;height:127px;background:var(--gold)"></div>
  <div class="nav" style="left:82px;top:7px"><span>HOME</span><span>ABOUT US</span><span>ITEMS</span><span>CONTACT US</span></div>
  <div class="ab" style="left:214px;top:7px;width:5px;height:3.5px;border-top:.6px solid #fff;border-bottom:.6px solid #fff"></div>
  <div class="ab" style="left:22px;top:20px;font-size:10px;font-weight:600">TM</div>
  <div class="ab title" style="left:22px;top:40px;font-size:11.5px;color:#fff">Introduction to<br>Ta Merosk</div>
  <div class="ab tiny" style="left:22px;top:78px;color:#dcdcf0;width:80px">Empowering Enterprises to Innovate through Intelligent Architecture, Automation &amp; AI</div>
  <div class="btn" style="left:25px;top:98px;background:var(--gold);color:#fff">More Info ›</div>
  <div class="btn" style="left:49px;top:98px;border:.4px solid #fff;color:#fff">See More ›</div>
  <div class="ab tiny" style="left:10px;bottom:8px;color:#fff">Presentation 2026</div>
  <div class="ab tiny" style="right:10px;bottom:8px;color:#fff">Next Slide ›</div>
</section>

<section class="slide" style="left:490.3px;top:29.7px">
  <div class="ab tiny" style="left:24px;top:21px;color:var(--ink)">Mar 20th, 2026<br><b>TM Group</b></div>
  <div class="ab tiny" style="left:104px;top:21px;color:var(--ink);text-align:center">TM Group<br><b>Presentation</b></div>
  <div class="ab tiny" style="right:24px;top:21px;color:var(--ink);text-align:right">Presented by<br><b>TM Group</b></div>
  <div class="ab title" style="left:0;right:0;top:50px;text-align:center;font-size:13px;color:var(--navy)">Introduction to<br>Ta <span class="gold">Merosk</span></div>
  <div class="ab tiny" style="left:0;right:0;top:88px;text-align:center;color:var(--ink);letter-spacing:.6px">February 2026</div>
  <div class="ab" style="left:0;right:0;top:104px;text-align:center;font-size:6px;font-weight:600;color:#b9b9c4">TM</div>
</section>

<section class="slide" style="left:721.7px;top:29.7px">
  <div class="photo photo-blue" role="img" aria-label="Hand touching an automation dashboard" style="left:0;top:0;width:227px;height:75px"></div>
  <div class="card" style="left:34px;top:48px;width:160px;height:60px"></div>
  <div class="ab" style="left:37px;top:61px;width:46px;height:7px;background:var(--navy);color:#fff;font-size:4px;padding-left:10px;line-height:7px">About Us</div>
  <div class="ab small" style="left:37px;top:75px;width:150px;font-size:2.9px">At Ta Merosk, we believe that technology should always enable and create value. Our mission is to empower our customers with seamless integration solutions and intelligent automation that transforms their operations and accelerates business growth.</div>
  <div class="foot"><b>TM</b>Introduction to Ta Merosk</div><div class="num">4</div>
</section>

<section class="slide" style="left:953.7px;top:29.7px">
  <div class="ab title" style="left:15px;top:12px;font-size:8.5px;font-weight:500"><span class="gold">Essential Elements of</span><br><span class="gold">a Robust</span> Financial Plan</div>
  <div class="ab tiny" style="left:15px;top:40px;width:110px">A robust financial plan is your guide to stability and growth; it should cover these key areas:</div>
  <div class="ab tiny" style="left:22px;top:60px;width:60px"><span class="tick"></span><b style="color:var(--ink)">Income Management</b> review your income sources and tactics to grow them.</div>
  <div class="ab tiny" style="left:22px;top:76px;width:60px"><span class="tick"></span><b style="color:var(--ink)">Expense and Debt</b> examine spending patterns to cut waste and clear debt.</div>
  <div class="ab tiny" style="left:88px;top:60px;width:60px"><span class="tick"></span><b style="color:var(--ink)">Savings Strategy</b> plans for setting aside income for future needs.</div>
  <div class="ab tiny" style="left:88px;top:76px;width:60px"><span class="tick"></span><b style="color:var(--ink)">Investment Planning</b> short and long-term plans to grow wealth.</div>
  <div class="ab tiny" style="left:154px;top:60px;width:62px"><span class="tick"></span><b style="color:var(--ink)">Risk and Insurance</b> provisions to guard against unexpected events.</div>
  <div class="ab tiny" style="left:154px;top:76px;width:62px"><span class="tick"></span><b style="color:var(--ink)">Retirement and Estate</b> long-term plan for a comfortable retirement.</div>
  <div class="foot"><b>TM</b>Introduction to Ta Merosk</div><div class="num">5</div>
</section>

<!-- Row 2 -->
<section class="slide white" style="left:28.6px;top:165.7px">
  <div class="ab title" style="left:20px;top:18px;font-size:12px;font-weight:500;color:var(--navy)">Agenda</div>
  <div class="ab small" style="left:19px;top:51px;line-height:3.4">01.&nbsp;&nbsp; About Us<br>02.&nbsp;&nbsp; Speakers Introduction<br>03.&nbsp;&nbsp; Our Expertises<br>04.&nbsp;&nbsp; Break time<br>05.&nbsp;&nbsp; Speakers<br>06.&nbsp;&nbsp; Free time</div>
  <div class="photo photo-office" role="img" aria-label="Team collaborating at a wall of sticky notes" style="left:128px;top:0;width:99px;height:116px"></div>
  <div class="ab" style="left:208px;top:74px;width:19px;height:42px;background:var(--gold)"></div>
</section>

<section class="slide" style="left:258.9px;top:165.7px">
  <div class="ab title" style="left:14px;top:17px;font-size:9px;font-weight:500">Decoding an<br><span class="gold">Investment</span><br><span class="gold">Report:</span> 8 Key<br>Components</div>
  <div class="ab tiny" style="left:14px;top:62px;width:70px">An investment report gives a full picture of a portfolio, its holdings, returns and risk. It helps track progress, judge strategy and guide better decisions about future allocations and goals across each market period.</div>
  <div class="ab tiny" style="left:90px;top:27px;width:62px"><span class="tick"></span><b style="color:var(--ink)">Executive Summary</b> brief overview of contents and overall results.</div>
  <div class="ab tiny" style="left:90px;top:47px;width:62px"><span class="tick"></span><b style="color:var(--ink)">Portfolio Overview</b> detailed breakdown of current holdings.</div>
  <div class="ab tiny" style="left:90px;top:67px;width:62px"><span class="tick"></span><b style="color:var(--ink)">Performance Analysis</b> returns against benchmarks.</div>
  <div class="ab tiny" style="left:90px;top:87px;width:62px"><span class="tick"></span><b style="color:var(--ink)">Risk Assessment</b> analysis of the portfolio risk profile.</div>
  <div class="ab tiny" style="left:155px;top:27px;width:62px"><span class="tick"></span><b style="color:var(--ink)">Asset Allocation</b> how assets are spread by category.</div>
  <div class="ab tiny" style="left:155px;top:47px;width:62px"><span class="tick"></span><b style="color:var(--ink)">Market Commentary</b> current market conditions.</div>
  <div class="ab tiny" style="left:155px;top:67px;width:62px"><span class="tick"></span><b style="color:var(--ink)">Recommendations</b> ways to improve the portfolio.</div>
  <div class="ab tiny" style="left:155px;top:87px;width:62px"><span class="tick"></span><b style="color:var(--ink)">Future Outlook</b> projections based on market trends.</div>
  <div class="foot"><b>TM</b>Introduction to Ta Merosk</div><div class="num">7</div>
</section>

<section class="slide" style="left:490.3px;top:165.7px">
  <div class="ab title" style="left:14px;top:9px;font-size:9px;font-weight:500">Pricing <span class="gold">Tables</span></div>
  <div class="plan" style="left:15px"><div class="head" style="background:var(--navy)">Starter Plan<b>25 $</b></div><ul><li>Financial Planning</li><li>Market Research</li><li>Risk Management</li><li>Marketing Strategy</li><li>IT Consulting</li><li>Human Resources</li><li>Mergers Guidance</li><li>Project Management</li></ul><div class="more" style="background:var(--navy)">More Info</div></div>
  <div class="plan" style="left:65px"><div class="head" style="background:var(--gold)">Growth Plan<b>50 $</b></div><ul><li>Financial Planning</li><li>Market Research</li><li>Risk Management</li><li>Marketing Strategy</li><li>IT Consulting</li><li>Human Resources</li><li>Mergers Guidance</li><li>Project Management</li></ul><div class="more" style="background:var(--gold)">More Info</div></div>
  <div class="plan" style="left:115px"><div class="head" style="background:var(--navy)">Premium Plan<b>99 $</b></div><ul><li>Financial Planning</li><li>Market Research</li><li>Risk Management</li><li>Marketing Strategy</li><li>IT Consulting</li><li>Human Resources</li><li>Mergers Guidance</li><li>Project Management</li></ul><div class="more" style="background:var(--navy)">More Info</div></div>
  <div class="plan" style="left:165px"><div class="head" style="background:var(--gold)">Enterprise Plan<b>100 $</b></div><ul><li>Financial Planning</li><li>Market Research</li><li>Risk Management</li><li>Marketing Strategy</li><li>IT Consulting</li><li>Human Resources</li><li>Mergers Guidance</li><li>Project Management</li></ul><div class="more" style="background:var(--gold)">More Info</div></div>
  <div class="foot"><b>TM</b>Introduction to Ta Merosk</div><div class="num">8</div>
</section>

<section class="slide" style="left:721.7px;top:165.7px">
  <div class="ab" style="left:126px;top:10px;width:25px;height:100px;background:#fff;box-shadow:0 0 3px rgba(0,0,0,.1)"></div>
  <table class="tbl" style="left:12px;top:17px;width:204px">
    <tr><th style="background:none"></th><th>Starter</th><th>Growth</th><th class="g">Premium</th><th>Enterprise</th><th>Best</th></tr>
    <tr><td>Price</td><td>$2,500</td><td>$3,700</td><td style="background:var(--navy);color:#fff">$6,600</td><td>$8,100</td><td>$15,000</td></tr>
    <tr><td>Business Strategy Consultation</td><td>✓</td><td>✓</td><td>✓</td><td>✓</td><td>✓</td></tr>
    <tr><td>Financial Planning Services</td><td>✓</td><td>✓</td><td>✓</td><td>✓</td><td>✓</td></tr>
    <tr><td>Market Research Analysis</td><td>✓</td><td>✓</td><td>✓</td><td>✓</td><td>✓</td></tr>
    <tr><td>Risk Management Assessment</td><td>✓</td><td>✓</td><td>✓</td><td>✓</td><td>✓</td></tr>
    <tr><td>Operational Efficiency Review</td><td>✓</td><td>✓</td><td>✓</td><td>✓</td><td>✓</td></tr>
    <tr><td>Branding and Marketing Strategy</td><td>✓</td><td>✓</td><td>✓</td><td>✓</td><td>✓</td></tr>
    <tr><td>IT Consulting Services</td><td>✓</td><td>✓</td><td>✓</td><td>✓</td><td>✓</td></tr>
    <tr><td>Human Resources Advisory</td><td></td><td>✓</td><td>✓</td><td>✓</td><td>✓</td></tr>
    <tr><td>Mergers and Acquisitions Guidance</td><td></td><td></td><td>✓</td><td>✓</td><td>✓</td></tr>
    <tr><td>Project Management Support</td><td></td><td></td><td>✓</td><td>✓</td><td>✓</td></tr>
    <tr><td>Regulatory Compliance Assistance</td><td></td><td></td><td></td><td>✓</td><td>✓</td></tr>
    <tr><td>Customer Experience Optimization</td><td></td><td></td><td></td><td></td><td>✓</td></tr>
  </table>
  <div class="foot"><b>TM</b>Introduction to Ta Merosk</div><div class="num">9</div>
</section>

<section class="slide" style="left:953.7px;top:165.7px">
  <div class="photo photo-office" role="img" aria-label="Smiling consultant in a suit" style="left:130px;top:0;width:97px;height:127px"></div>
  <div class="ab title" style="left:15px;top:13px;font-size:9px;font-weight:500">Transforming <span class="gold">Financial</span><br><span class="gold">Strategy</span> with Expert<br>Guidance</div>
  <div class="ab" style="left:15px;top:50px;width:125px;height:60px;background:#fff"></div>
  <div class="ab tiny" style="left:22px;top:57px;width:110px;font-style:italic">“The consulting team transformed our financial strategy with deep understanding of our needs. They crafted a clear roadmap for our future, enabling effective decision-making and resource optimization. Their professionalism is commendable.”</div>
  <div class="ab" style="left:15px;top:93px;width:125px;height:16px;background:var(--navy);color:#fff;padding:3px 6px;font-size:3px"><b style="font-weight:600">Mira Solen</b><br><span style="font-size:2.4px">Chief Executive Officer</span></div>
  <div class="foot"><b>TM</b>Introduction to Ta Merosk</div><div class="num" style="color:#fff">10</div>
</section>

<!-- Row 3 -->
<section class="slide" style="left:28.6px;top:301.1px">
  <div class="photo photo-blue" role="img" aria-label="Finger pointing at digital automation interface" style="left:15px;top:13px;width:197px;height:55px;border-radius:2px"></div>
  <div class="ab title" style="left:24px;top:20px;font-size:8.5px;font-weight:500;color:#fff">Financial Blueprint for<br>Future Growth</div>
  <div class="ab tiny" style="left:24px;top:44px;width:100px;color:#e3e3f5">This project involved a complete financial plan for a rapidly growing tech company, designed to support its goals while ensuring stability.</div>
  <div class="card" style="left:15px;top:74px;width:61px;height:36px"><div class="tiny" style="padding:4px"><span style="color:var(--navy)">◎</span><br><b style="color:var(--ink)">Complexity</b> The project demanded a deep understanding of the client.</div></div>
  <div class="card" style="left:83px;top:74px;width:61px;height:36px"><div class="tiny" style="padding:4px"><span class="gold">⚙</span><br><b style="color:var(--ink)">Impact</b> The plan shaped the client’s business strategy and success.</div></div>
  <div class="card" style="left:151px;top:74px;width:61px;height:36px"><div class="tiny" style="padding:4px"><span style="color:var(--navy)">♟</span><br><b style="color:var(--ink)">Innovation</b> Balancing aggressive growth with prudence.</div></div>
  <div class="foot"><b>TM</b>Introduction to Ta Merosk</div><div class="num">11</div>
</section>

<section class="slide" style="left:258.9px;top:301.1px">
  <div class="photo photo-violet" role="img" aria-label="Person writing at a desk, violet tint" style="left:15px;top:16px;width:125px;height:90px;border-radius:2px"></div>
  <div class="ab title" style="left:26px;top:36px;font-size:8.5px;font-weight:500;color:#fff">Financial<br>Blueprint for<br>Future Growth</div>
  <div class="ab tiny" style="left:26px;top:74px;width:82px;color:#eee">This project involved a complete financial plan for a rapidly growing tech company, designed to support its goals while ensuring stability.</div>
  <div class="card" style="left:145px;top:16px;width:67px;height:27px"><div class="tiny" style="padding:3px 5px"><span style="color:var(--navy)">◎</span><br><b style="color:var(--ink)">Complexity</b> The project demanded a deep grasp of the industry.</div></div>
  <div class="card" style="left:145px;top:47px;width:67px;height:27px"><div class="tiny" style="padding:3px 5px"><span class="gold">⚙</span><br><b style="color:var(--ink)">Impact</b> The plan shaped the client’s strategy and success.</div></div>
  <div class="card" style="left:145px;top:78px;width:67px;height:28px"><div class="tiny" style="padding:3px 5px"><span style="color:var(--navy)">♟</span><br><b style="color:var(--ink)">Innovation</b> Balancing aggressive growth with prudence.</div></div>
  <div class="foot"><b>TM</b>Introduction to Ta Merosk</div><div class="num">12</div>
</section>

<section class="slide" style="left:490.3px;top:301.1px">
  <div class="ab title" style="left:16px;top:12px;font-size:8.5px;font-weight:500"><span>Financial</span> <span class="gold">Blueprint</span><br>for Future Growth</div>
  <div class="ab tiny" style="left:118px;top:18px;width:95px">This project involved a full financial plan for a fast growing tech company, built to support its goals while ensuring stability.</div>
  <div class="card" style="left:16px;top:42px;width:94px;height:68px"></div>
  <div class="ab tiny" style="left:20px;top:47px;width:86px"><span style="color:var(--navy)">◎</span> <b style="color:var(--ink)">Complexity</b> The project demanded a deep grasp of the industry.</div>
  <div class="ab" style="left:20px;top:64px;width:86px;height:.4px;background:var(--line)"></div>
  <div class="ab tiny" style="left:20px;top:68px;width:86px"><span class="gold">⚙</span> <b style="color:var(--ink)">Impact</b> The plan shaped the client’s strategy and success.</div>
  <div class="ab" style="left:20px;top:85px;width:86px;height:.4px;background:var(--line)"></div>
  <div class="ab tiny" style="left:20px;top:89px;width:86px"><span style="color:var(--navy)">♟</span> <b style="color:var(--ink)">Innovation</b> Balancing aggressive growth with prudence.</div>
  <div class="photo photo-violet" role="img" aria-label="Chess knight piece, violet tint" style="left:116px;top:42px;width:95px;height:68px;border-radius:2px"></div>
  <div class="ab tiny" style="left:121px;top:95px;color:#fff">Financial Blueprint for<br>Future Growth</div>
  <div class="foot"><b>TM</b>Introduction to Ta Merosk</div><div class="num">13</div>
</section>

<section class="slide" style="left:721.7px;top:301.1px">
  <div class="photo photo-violet" role="img" aria-label="Two colleagues reviewing work on a laptop" style="left:15px;top:16px;width:125px;height:90px;border-radius:2px"></div>
  <div class="ab title" style="left:22px;top:74px;font-size:6px;font-weight:500;color:#fff">Financial<br>Blueprint<br>for Future<br>Growth</div>
  <div class="ab tiny" style="left:62px;top:82px;width:72px;color:#eee">This project involved a complete financial plan for a fast growing tech company.</div>
  <div class="ab" style="left:145px;top:16px;width:1px;height:90px;background:var(--navy)"></div>
  <div class="card" style="left:146px;top:16px;width:66px;height:28px"><div class="tiny" style="padding:4px"><b style="color:var(--ink)">Complexity</b> The project demanded a deep grasp of the industry.</div></div>
  <div class="card" style="left:146px;top:47px;width:66px;height:28px"><div class="tiny" style="padding:4px"><b style="color:var(--ink)">Impact</b> The plan shaped the client’s strategy and success.</div></div>
  <div class="card" style="left:146px;top:78px;width:66px;height:28px"><div class="tiny" style="padding:4px"><b style="color:var(--ink)">Innovation</b> Balancing aggressive growth with prudence.</div></div>
  <div class="foot"><b>TM</b>Introduction to Ta Merosk</div><div class="num">14</div>
</section>

<section class="slide" style="left:953.7px;top:301.1px">
  <div class="ab title" style="left:15px;top:15px;font-size:9.5px;font-weight:500">OUR <span class="gold">EXPERTISE</span></div>
  <div class="ab" style="left:115px;top:38px;width:44px;height:73px;background:var(--navy)"></div>
  <div class="avatar" role="img" aria-label="Portrait" style="left:31px;top:46px;width:17px;height:17px"></div>
  <div class="avatar" role="img" aria-label="Portrait" style="left:79px;top:46px;width:17px;height:17px"></div>
  <div class="avatar ring" role="img" aria-label="Portrait" style="left:128px;top:46px;width:17px;height:17px"></div>
  <div class="avatar" role="img" aria-label="Portrait" style="left:176px;top:46px;width:17px;height:17px"></div>
  <div class="person" style="left:22px;top:66px"><div class="name">Ana Pell</div><div class="role">CEO/Founder</div><div class="tiny" style="margin-top:2px">A peep at some distant orb has power to raise and purify.</div></div>
  <div class="person" style="left:70px;top:66px"><div class="name">Lia Moor</div><div class="role">CEO/Founder</div><div class="tiny" style="margin-top:2px">A peep at some distant orb has power to raise and purify.</div></div>
  <div class="person" style="left:119px;top:66px;color:#fff"><div class="name">Tom Reyes</div><div class="role">CEO/Founder</div><div class="tiny" style="margin-top:2px;color:#d8d8f0">A peep at some distant orb has power to raise and purify.</div></div>
  <div class="person" style="left:167px;top:66px"><div class="name">Ben Arlo</div><div class="role">CEO/Founder</div><div class="tiny" style="margin-top:2px">A peep at some distant orb has power to raise and purify.</div></div>
  <div class="ab" style="left:15px;top:109px;width:197px;height:.6px;background:var(--gold)"></div>
  <div class="foot"><b>TM</b>Introduction to Ta Merosk</div><div class="num">15</div>
</section>

<!-- Row 4 -->
<section class="slide" style="left:28.6px;top:436.6px">
  <div class="ab title" style="left:15px;top:15px;font-size:9.5px;font-weight:500;color:var(--navy)">OUR <span class="gold">EXPERTISE</span></div>
  <div class="ab" style="left:15px;top:44px;width:197px;height:41px;background:var(--navy)"></div>
  <div class="ab" style="left:15px;top:44px;width:47px;height:41px;background:var(--gold)"></div>
  <div class="avatar ring" role="img" aria-label="Portrait" style="left:25px;top:40px;width:25px;height:25px;border-color:var(--navy)"></div>
  <div class="avatar ring" role="img" aria-label="Portrait" style="left:80px;top:40px;width:25px;height:25px;border-color:var(--gold)"></div>
  <div class="avatar ring" role="img" aria-label="Portrait" style="left:121px;top:40px;width:25px;height:25px;border-color:var(--gold)"></div>
  <div class="avatar ring" role="img" aria-label="Portrait" style="left:163px;top:40px;width:25px;height:25px;border-color:var(--gold)"></div>
  <div class="person" style="left:20px;top:69px;color:#fff"><div class="name">Ivo Kest</div><div class="role">Job position here</div></div>
  <div class="person" style="left:75px;top:69px;color:#fff"><div class="name">Dan Hollis</div><div class="role">Job position here</div></div>
  <div class="person" style="left:116px;top:69px;color:#fff"><div class="name">Dora Vale</div><div class="role">Job position here</div></div>
  <div class="person" style="left:158px;top:69px;color:#fff"><div class="name">Tim Rowe</div><div class="role">Job position here</div></div>
  <div class="foot"><b>TM</b>Introduction to Ta Merosk</div><div class="num">16</div>
</section>

<section class="slide navy" style="left:258.9px;top:436.6px">
  <div class="ab title" style="left:0;right:0;top:9px;text-align:center;font-size:9.5px;font-weight:500;color:#fff">OUR <span class="gold">EXPERTISE</span></div>
  <div class="avatar ring" role="img" aria-label="Portrait" style="left:45px;top:29px;width:21px;height:21px"></div>
  <div class="avatar ring" role="img" aria-label="Portrait" style="left:103px;top:29px;width:21px;height:21px"></div>
  <div class="avatar ring" role="img" aria-label="Portrait" style="left:161px;top:29px;width:21px;height:21px"></div>
  <div class="avatar ring" role="img" aria-label="Portrait" style="left:45px;top:77px;width:21px;height:21px"></div>
  <div class="avatar ring" role="img" aria-label="Portrait" style="left:103px;top:77px;width:21px;height:21px"></div>
  <div class="avatar ring" role="img" aria-label="Portrait" style="left:161px;top:77px;width:21px;height:21px"></div>
  <div class="person" style="left:37px;top:53px"><div class="name">Wendy Lark</div><div class="role gold">Job position here</div></div>
  <div class="person" style="left:95px;top:53px"><div class="name">Joel Marsh</div><div class="role gold">Job position here</div></div>
  <div class="person" style="left:153px;top:53px"><div class="name">Carl Penn</div><div class="role gold">Job position here</div></div>
  <div class="person" style="left:37px;top:101px"><div class="name">Ella Hart</div><div class="role gold">Job position here</div></div>
  <div class="person" style="left:95px;top:101px"><div class="name">Rob Dale</div><div class="role gold">Job position here</div></div>
  <div class="person" style="left:153px;top:101px"><div class="name">Mara Gill</div><div class="role gold">Job position here</div></div>
</section>

<section class="slide" style="left:490.3px;top:436.6px">
  <div class="ab title" style="left:15px;top:11px;font-size:9px;font-weight:500">Stages of <span class="gold">Financial</span> Planning</div>
  <div class="ab tiny" style="left:15px;top:27px;width:170px">Financial planning is a systematic process that helps organizations define and achieve their long-term goals.</div>
  <div class="ab small" style="left:26px;top:39px;font-weight:500">Key Stages:</div>
  <div class="ab tiny" style="left:18px;top:46px;width:92px;line-height:1.9"><span class="tick"></span><b style="color:var(--ink)">Goal Setting</b> define clear, measurable goals.<br><span class="tick"></span><b style="color:var(--ink)">Data Gathering</b> collect the relevant financial data.<br><span class="tick"></span><b style="color:var(--ink)">Analysis</b> evaluate strengths and weaknesses.<br><span class="tick"></span><b style="color:var(--ink)">Plan Development</b> create the full financial plan.<br><span class="tick"></span><b style="color:var(--ink)">Implementation</b> execute the plan and monitor.<br><span class="tick"></span><b style="color:var(--ink)">Review and Update</b> revise the plan regularly.</div>
  <div class="ab small" style="left:117px;top:39px;font-weight:500">Key Performance Indicators (KPIs):</div>
  <div class="card" style="left:117px;top:47px;width:45px;height:26px;text-align:center;font-size:2.6px;padding-top:6px"><span style="color:var(--navy)">▣</span><br><b>Budget<br>Adherence</b></div>
  <div class="card" style="left:167px;top:47px;width:45px;height:26px;text-align:center;font-size:2.6px;padding-top:6px"><span style="color:var(--navy)">●</span><br><b>Savings<br>Rate</b></div>
  <div class="card" style="left:117px;top:78px;width:45px;height:26px;text-align:center;font-size:2.6px;padding-top:6px"><span style="color:var(--navy)">▤</span><br><b>Debt-to-<br>Income Ratio</b></div>
  <div class="card" style="left:167px;top:78px;width:45px;height:26px;text-align:center;font-size:2.6px;padding-top:6px"><span style="color:var(--navy)">▦</span><br><b>Investment<br>Return</b></div>
  <div class="foot"><b>TM</b>Introduction to Ta Merosk</div><div class="num">18</div>
</section>

<section class="slide" style="left:721.7px;top:436.6px">
  <div class="ab title" style="left:14px;top:27px;font-size:8.5px;font-weight:500">Crafting a Successful<br><span class="gold">Investment Plan</span>:<br>Key Considerations</div>
  <div class="ab tiny" style="left:14px;top:61px;width:105px">Creating a robust investment plan begins with clear, defined goals that are specific, measurable and time-bound. It is equally important to know your risk tolerance, which guides your asset choices and diversification strategy and shapes how the plan evolves with market conditions.</div>
  <div class="bubble" style="left:134px;top:24px;width:45px;height:45px;background:var(--navy);color:#fff;font-size:3.4px">Investment<br>Goals</div>
  <div class="bubble" style="left:164px;top:59px;width:34px;height:34px;background:var(--gold-soft);color:#fff;font-size:3.2px">Risk<br>Tolerance</div>
  <div class="bubble" style="left:180px;top:30px;width:24px;height:24px;background:#b0abe0;color:#fff">Asset<br>Allocation</div>
  <div class="bubble" style="left:146px;top:3px;width:18px;height:18px;background:#fff;box-shadow:0 0 2px rgba(0,0,0,.1)">Costs</div>
  <div class="bubble" style="left:169px;top:11px;width:16px;height:16px;background:#fff;box-shadow:0 0 2px rgba(0,0,0,.1);font-size:2px">Diversifi<br>cation</div>
  <div class="bubble" style="left:200px;top:10px;width:18px;height:18px;background:#fff;box-shadow:0 0 2px rgba(0,0,0,.1);font-size:2px">Emergency<br>Fund</div>
  <div class="bubble" style="left:125px;top:69px;width:18px;height:18px;background:#fff;box-shadow:0 0 2px rgba(0,0,0,.1);font-size:2px">Investment<br>Time Horizon</div>
  <div class="bubble" style="left:143px;top:94px;width:16px;height:16px;background:#fff;box-shadow:0 0 2px rgba(0,0,0,.1);font-size:2px">Liquidity<br>Needs</div>
  <div class="bubble" style="left:166px;top:98px;width:20px;height:20px;background:#fff;box-shadow:0 0 2px rgba(0,0,0,.1);font-size:2px">Tax<br>Factors</div>
  <div class="bubble" style="left:208px;top:55px;width:18px;height:18px;background:#fff;box-shadow:0 0 2px rgba(0,0,0,.1);font-size:2px">Perform<br>Measure</div>
  <div class="foot"><b>TM</b>Introduction to Ta Merosk</div>
</section>

<section class="slide" style="left:953.7px;top:436.6px">
  <div class="ab title" style="left:15px;top:11px;font-size:8.5px;font-weight:500">Crafting an <span class="gold">Investment Strategy</span>:<br>A Six-Step Process</div>
  <div class="ab" style="left:15px;top:43px;width:197px;height:.4px;background:var(--line)"></div>
  <div class="ab" style="left:15px;top:84px;width:197px;height:.4px;background:var(--line)"></div>
  <div class="ab tiny" style="left:15px;top:46px;width:62px"><b style="color:var(--ink)">01 · Identifying Goals</b><br>Define what you want to achieve with your investments, short or long-term.</div>
  <div class="ab tiny" style="left:82px;top:46px;width:62px"><b style="color:var(--ink)">03 · Asset Allocation</b><br>Based on goals and risk, decide how to spread across asset classes.</div>
  <div class="ab tiny" style="left:149px;top:46px;width:63px"><b style="color:var(--ink)">05 · Implementation</b><br>Put the plan into action, considering timing and costs.</div>
  <div class="ab tiny" style="left:15px;top:88px;width:62px"><b style="color:var(--ink)">02 · Risk Tolerance</b><br>Assess how much risk you can accept and how it shapes your choices.</div>
  <div class="ab tiny" style="left:82px;top:88px;width:62px"><b style="color:var(--ink)">04 · Selection</b><br>Choose specific stocks, bonds or funds that track your aims.</div>
  <div class="ab tiny" style="left:149px;top:88px;width:63px"><b style="color:var(--ink)">06 · Monitoring</b><br>Review regularly and adjust as markets and goals change.</div>
  <div class="foot"><b>TM</b>Introduction to Ta Merosk</div><div class="num">20</div>
</section>

<!-- Row 5 -->
<section class="slide white" style="left:28.6px;top:569.1px">
  <div class="ab firm-name" style="left:0;right:0;top:56px;text-align:center">Halvard Law Firm</div>
</section>

<section class="slide" style="left:258.9px;top:569.1px">
  <div class="tabs"><span>Investment Overview</span><span>Performance Metrics</span><span>Risk Assessment</span><span>Investment Timeline</span><span>Financial Projections</span></div>
  <div class="card" style="left:14px;top:20px;width:48px;height:22px;padding:4px"><div style="font-size:6px;font-weight:600;color:var(--navy)">+570K <span class="gold" style="font-size:3px">▲</span></div><div class="tiny">Lorem ipsum dolor sit amet</div></div>
  <div class="card" style="left:66px;top:20px;width:147px;height:22px"></div>
  <svg class="ab" style="left:70px;top:23px" width="16" height="16"><circle cx="8" cy="8" r="6" fill="none" stroke="var(--line)" stroke-width="1.5"/><path d="M8 2 A6 6 0 1 1 2.5 10" fill="none" stroke="var(--navy)" stroke-width="1.5"/></svg>
  <div class="ab tiny" style="left:90px;top:25px;width:115px"><b style="color:var(--navy)">Progress:</b> <b style="color:var(--ink)">implementation of the plan</b><br>Lorem ipsum dolor sit amet, sed do tempor incididunt ut labore.</div>
  <div class="card" style="left:14px;top:46px;width:48px;height:66px"></div>
  <svg class="ab" style="left:22px;top:53px" width="32" height="32"><circle cx="16" cy="16" r="15" fill="var(--navy)"/><circle cx="16" cy="19" r="9" fill="var(--gold)"/><circle cx="16" cy="21" r="5" fill="#b0abe0"/></svg>
  <div class="ab tiny" style="left:20px;top:92px">● Stage 1 &nbsp;● Stage 2<br>&nbsp;&nbsp;&nbsp;&nbsp;● Stage 3</div>
  <div class="card" style="left:66px;top:46px;width:147px;height:66px"></div>
  <div class="ab small" style="left:72px;top:50px;font-weight:500">Description of current investment projects</div>
  <svg class="ab" style="left:72px;top:58px" width="136" height="50">
    <g fill="#e6e6ee"><rect x="8" y="4" width="4" height="38" rx="2"/><rect x="31" y="4" width="4" height="38" rx="2"/><rect x="54" y="4" width="4" height="38" rx="2"/><rect x="77" y="4" width="4" height="38" rx="2"/><rect x="100" y="4" width="4" height="38" rx="2"/><rect x="123" y="4" width="4" height="38" rx="2"/></g>
    <rect x="8" y="26" width="4" height="16" rx="2" fill="var(--navy)"/><rect x="54" y="30" width="4" height="12" rx="2" fill="var(--navy)"/><rect x="77" y="10" width="4" height="32" rx="2" fill="var(--gold)"/><rect x="100" y="24" width="4" height="18" rx="2" fill="var(--navy)"/><rect x="123" y="28" width="4" height="14" rx="2" fill="var(--gold)"/><rect x="31" y="20" width="4" height="22" rx="2" fill="#b0abe0"/>
    <g font-size="2.4" fill="#8a8a99"><text x="5" y="48">Project</text><text x="28" y="48">Project</text><text x="51" y="48">Project</text><text x="74" y="48">Project</text><text x="97" y="48">Project</text><text x="120" y="48">Project</text></g>
  </svg>
  <div class="foot"><b>TM</b>Introduction to Ta Merosk</div><div class="num">22</div>
</section>

<section class="slide" style="left:490.3px;top:569.1px">
  <div class="tabs"><span>Investment Overview</span><span>Performance Metrics</span><span>Risk Assessment</span><span>Investment Timeline</span><span>Financial Projections</span></div>
  <div class="card" style="left:14px;top:20px;width:90px;height:24px;padding:4px"><div class="tiny"><b style="color:var(--navy)">Progress:</b> <b style="color:var(--ink)">implementation of the plan</b></div><div style="height:2.5px;background:#e6e6ee;border-radius:2px;margin-top:6px"><div style="width:65%;height:100%;background:var(--navy);border-radius:2px"></div></div></div>
  <div class="ab" style="left:108px;top:20px;width:38px;height:24px;background:var(--gold);color:#fff;font-size:6px;font-weight:600;display:flex;align-items:center;justify-content:center">+570K</div>
  <div class="ab tiny" style="left:150px;top:22px;width:62px">Lorem ipsum dolor sit amet, sed do tempor incididunt ut labore et dolore magna.</div>
  <div class="card" style="left:14px;top:48px;width:90px;height:64px"></div>
  <svg class="ab" style="left:26px;top:54px" width="70" height="22"><circle cx="11" cy="11" r="9" fill="none" stroke="#e6e6ee" stroke-width="1.4"/><path d="M11 2A9 9 0 1 1 3 15" fill="none" stroke="var(--navy)" stroke-width="1.4"/><circle cx="58" cy="11" r="9" fill="none" stroke="#e6e6ee" stroke-width="1.4"/><path d="M58 2A9 9 0 1 1 50 15" fill="none" stroke="var(--navy)" stroke-width="1.4"/><text x="6" y="12" font-size="3.4" font-weight="600" fill="#1b1a4f">20YY</text><text x="53" y="12" font-size="3.4" font-weight="600" fill="#1b1a4f">20YY</text></svg>
  <div class="ab tiny" style="left:20px;top:82px;width:34px;text-align:center"><b style="color:var(--ink)">Description</b><br>Lorem ipsum dolor sit amet</div>
  <div class="ab tiny" style="left:65px;top:82px;width:34px;text-align:center"><b style="color:var(--ink)">Description</b><br>Lorem ipsum dolor sit amet</div>
  <div class="card" style="left:108px;top:48px;width:105px;height:64px"></div>
  <div class="ab tiny" style="left:113px;top:52px"><b style="color:var(--navy)">Progress:</b> <b style="color:var(--ink)">implementation of the plan</b></div>
  <svg class="ab" style="left:113px;top:60px" width="96" height="48"><g stroke="#eee" stroke-width=".3"><line x1="4" y1="6" x2="94" y2="6"/><line x1="4" y1="16" x2="94" y2="16"/><line x1="4" y1="26" x2="94" y2="26"/><line x1="4" y1="36" x2="94" y2="36"/></g>
  <g fill="var(--navy)"><rect x="10" y="26" width="2" height="14"/><rect x="28" y="30" width="2" height="10"/><rect x="46" y="18" width="2" height="22"/><rect x="64" y="22" width="2" height="18"/><rect x="82" y="28" width="2" height="12"/></g>
  <g fill="var(--gold)"><rect x="13" y="30" width="2" height="10"/><rect x="31" y="24" width="2" height="16"/><rect x="49" y="28" width="2" height="12"/><rect x="67" y="14" width="2" height="26"/><rect x="85" y="32" width="2" height="8"/></g></svg>
  <div class="foot"><b>TM</b>Introduction to Ta Merosk</div><div class="num">23</div>
</section>

<section class="slide" style="left:721.7px;top:569.1px">
  <div class="tabs"><span>Investment Overview</span><span>Performance Metrics</span><span>Risk Assessment</span><span>Investment Timeline</span><span>Financial Projections</span></div>
  <div class="card" style="left:14px;top:20px;width:98px;height:24px"></div>
  <div class="ab tiny" style="left:18px;top:23px;width:45px">Lorem ipsum dolor sit amet, sed do tempor incididunt ut labore.</div>
  <div class="ab" style="left:66px;top:22px;width:43px;height:20px;background:var(--navy);color:#fff;text-align:center;padding-top:2px"><div style="font-size:6px;font-weight:600">860K</div><div style="font-size:2.2px">Lorem ipsum dolor</div></div>
  <div class="card" style="left:116px;top:20px;width:97px;height:24px"></div>
  <div class="ab tiny" style="left:120px;top:24px"><b style="color:var(--ink)">Lorem ipsum</b><br>dolor sit<br><b style="color:var(--ink);font-size:3.2px">+78%</b></div>
  <div class="ab" style="left:138px;top:24px;font-size:5px;color:var(--navy);letter-spacing:.6px">♟♟♟♟♟♟♟♟♟<br>♟♟♟</div>
  <div class="card" style="left:14px;top:48px;width:98px;height:64px"></div>
  <div class="ab small" style="left:20px;top:52px;font-weight:500">Description of current investment projects</div>
  <svg class="ab" style="left:20px;top:60px" width="88" height="48"><path d="M2 40 L20 34 L40 30 L58 22 L70 12 L86 26 L86 42 L2 42 Z" fill="#7a74c7"/><g stroke="#eee" stroke-width=".3"><line x1="2" y1="10" x2="86" y2="10"/><line x1="2" y1="20" x2="86" y2="20"/><line x1="2" y1="30" x2="86" y2="30"/></g></svg>
  <div class="card" style="left:116px;top:48px;width:97px;height:30px"></div>
  <div class="card" style="left:116px;top:82px;width:97px;height:30px"></div>
  <svg class="ab" style="left:120px;top:52px" width="90" height="56"><circle cx="8" cy="10" r="6" fill="none" stroke="#b0abe0" stroke-width="1.2"/><circle cx="8" cy="44" r="6" fill="none" stroke="#b0abe0" stroke-width="1.2"/>
  <g fill="var(--gold)"><rect x="30" y="12" width="2.5" height="6"/><rect x="44" y="10" width="2.5" height="8"/><rect x="58" y="4" width="2.5" height="14"/><rect x="72" y="6" width="2.5" height="12"/></g><g fill="var(--navy)"><rect x="34" y="14" width="2.5" height="4"/><rect x="48" y="12" width="2.5" height="6"/><rect x="62" y="8" width="2.5" height="10"/></g>
  <g fill="var(--navy)"><rect x="30" y="44" width="2.5" height="8"/><rect x="44" y="46" width="2.5" height="6"/><rect x="58" y="40" width="2.5" height="12"/><rect x="72" y="38" width="2.5" height="14"/></g><g fill="#b0abe0"><rect x="34" y="48" width="2.5" height="4"/><rect x="48" y="44" width="2.5" height="8"/><rect x="62" y="46" width="2.5" height="6"/></g></svg>
  <div class="foot"><b>TM</b>Introduction to Ta Merosk</div><div class="num">24</div>
</section>

<section class="slide" style="left:953.7px;top:569.1px">
  <div class="tabs"><span>Investment Overview</span><span>Performance Metrics</span><span>Risk Assessment</span><span>Investment Timeline</span><span>Financial Projections</span></div>
  <div class="card" style="left:14px;top:20px;width:95px;height:92px"></div>
  <svg class="ab" style="left:17px;top:24px" width="89" height="86">
    <rect x="0" y="0" width="89" height="5" fill="var(--navy)"/>
    <g font-size="2" fill="#fff"><text x="26" y="3.5">M1</text><text x="36" y="3.5">M2</text><text x="46" y="3.5">M3</text><text x="56" y="3.5">M4</text><text x="66" y="3.5">M5</text><text x="76" y="3.5">M6</text></g>
    <rect x="36" y="5" width="12" height="80" fill="#e7ecf8"/>
    <g font-size="2" fill="#1b1a4f"><text x="1" y="11">Investment 01</text><text x="1" y="19">Investment 02</text><text x="1" y="27">Investment 03</text><text x="1" y="35">Investment 04</text><text x="1" y="43">Investment 05</text><text x="1" y="51">Investment 06</text><text x="1" y="59">Investment 07</text><text x="1" y="67">Investment 08</text><text x="1" y="75">Investment 09</text></g>
    <g fill="var(--gold)"><rect x="28" y="9" width="30" height="2"/><rect x="40" y="33" width="26" height="2"/><rect x="32" y="57" width="22" height="2"/></g>
    <g fill="var(--navy)"><rect x="38" y="17" width="34" height="2"/><rect x="26" y="25" width="20" height="2"/><rect x="48" y="41" width="30" height="2"/><rect x="30" y="49" width="36" height="2"/><rect x="44" y="65" width="30" height="2"/><rect x="34" y="73" width="26" height="2"/></g>
  </svg>
  <div class="card" style="left:113px;top:20px;width:100px;height:28px"></div>
  <div class="card" style="left:113px;top:52px;width:100px;height:28px"></div>
  <div class="card" style="left:113px;top:84px;width:100px;height:28px"></div>
  <svg class="ab" style="left:116px;top:24px" width="95" height="86">
    <g fill="none" stroke-width="1.2"><circle cx="8" cy="10" r="6" stroke="#e6e6ee"/><path d="M8 4A6 6 0 0 1 14 10" stroke="var(--gold)"/><circle cx="8" cy="42" r="6" stroke="#e6e6ee"/><path d="M8 36A6 6 0 0 1 13 39" stroke="var(--gold)"/><circle cx="8" cy="74" r="6" stroke="#e6e6ee"/><path d="M8 68A6 6 0 0 1 14 74" stroke="var(--gold)"/></g>
    <g font-size="2.4" font-weight="600" fill="#1b1a4f"><text x="4" y="11">+15%</text><text x="5" y="43">+8%</text><text x="4" y="75">+25%</text></g>
    <g font-size="2.2" fill="#1b1a4f"><text x="20" y="6"><tspan fill="#c9a95c">Progress:</tspan></text><text x="20" y="9">implementation of the plan</text><text x="20" y="38"><tspan fill="#c9a95c">Progress:</tspan></text><text x="20" y="41">implementation of the plan</text><text x="20" y="70"><tspan fill="#c9a95c">Progress:</tspan></text><text x="20" y="73">implementation of the plan</text></g>
    <g><rect x="20" y="13" width="48" height="2" rx="1" fill="#e6e6ee"/><rect x="20" y="13" width="36" height="2" rx="1" fill="var(--navy)"/><rect x="20" y="45" width="48" height="2" rx="1" fill="#e6e6ee"/><rect x="20" y="45" width="28" height="2" rx="1" fill="var(--navy)"/><rect x="20" y="77" width="48" height="2" rx="1" fill="#e6e6ee"/><rect x="20" y="77" width="40" height="2" rx="1" fill="var(--navy)"/></g>
    <g font-size="2" fill="#8a8a99"><text x="72" y="10">Lorem ipsum</text><text x="72" y="13">dolor sit amet</text><text x="72" y="42">Lorem ipsum</text><text x="72" y="45">dolor sit amet</text><text x="72" y="74">Lorem ipsum</text><text x="72" y="77">dolor sit amet</text></g>
  </svg>
  <div class="foot"><b>TM</b>Introduction to Ta Merosk</div><div class="num">25</div>
</section>

<!-- Row 6 -->
<section class="slide" style="left:28.6px;top:704px">
  <div class="tabs"><span>Investment Overview</span><span>Performance Metrics</span><span>Risk Assessment</span><span>Investment Timeline</span><span>Financial Projections</span></div>
  <div class="card" style="left:14px;top:20px;width:95px;height:24px"></div>
  <div class="ab tiny" style="left:18px;top:24px"><b style="color:var(--ink)">Lorem ipsum</b><br>dolor sit<br>amet<br><b style="color:var(--ink);font-size:3.2px">+78%</b></div>
  <div class="ab" style="left:38px;top:24px;font-size:5px;color:var(--navy);letter-spacing:.6px">♟♟♟♟♟♟♟♟♟<br>♟♟♟</div>
  <div class="ab" style="left:93px;top:24px;width:13px;height:16px;background:#7a74c7;border-radius:1px"></div>
  <div class="card" style="left:113px;top:20px;width:100px;height:24px"></div>
  <svg class="ab" style="left:116px;top:23px" width="94" height="18"><path d="M4 14 C18 4, 26 8, 38 10 S 60 2, 72 8 S 86 6, 92 4" fill="none" stroke="#9fb7e8" stroke-width=".7"/><path d="M4 12 C20 14, 30 6, 44 9 S 70 12, 92 10" fill="none" stroke="var(--navy)" stroke-width=".7"/></svg>
  <div class="card" style="left:14px;top:48px;width:95px;height:64px"></div>
  <svg class="ab" style="left:20px;top:54px" width="40" height="40"><circle cx="20" cy="20" r="16" fill="none" stroke="#e6e6ee" stroke-width="2"/><path d="M20 4A16 16 0 1 1 6 28" fill="none" stroke="var(--navy)" stroke-width="2"/><path d="M6 28A16 16 0 0 1 20 4" fill="none" stroke="var(--gold)" stroke-width="2"/><path d="M16 16 h8 l-4 6z" fill="var(--navy)"/></svg>
  <div class="ab tiny" style="left:64px;top:57px;width:42px"><b style="color:var(--ink);font-size:3px">Description:</b><br>Lorem ipsum dolor sit amet, consectetur adipiscing elit, sed do tempor incididunt ut labore.</div>
  <div class="card" style="left:113px;top:48px;width:100px;height:64px"></div>
  <div class="ab tiny" style="left:118px;top:52px"><b style="color:var(--navy)">Progress:</b> <b style="color:var(--ink)">financial projections</b></div>
  <div class="ab" style="left:118px;top:60px;width:90px;height:2.5px;background:#e6e6ee;border-radius:2px"><div style="width:58%;height:100%;background:#7a74c7;border-radius:2px"></div></div>
  <div class="ab tiny" style="left:118px;top:70px;width:34px">Lorem ipsum dolor sit amet, sed do tempor incididunt.</div>
  <div class="calendar" style="left:160px;top:68px">
    <span class="dow">S</span><span class="dow">M</span><span class="dow">T</span><span class="dow">W</span><span class="dow">T</span><span class="dow">F</span><span class="dow">S</span>
    <span>1</span><span>2</span><span>3</span><span class="on">4</span><span>5</span><span>6</span><span>7</span>
    <span>8</span><span>9</span><span>10</span><span>11</span><span>12</span><span class="on">13</span><span>14</span>
    <span>15</span><span>16</span><span>17</span><span>18</span><span>19</span><span>20</span><span>21</span>
    <span>22</span><span class="on">23</span><span>24</span><span>25</span><span>26</span><span>27</span><span>28</span>
  </div>
  <div class="foot"><b>TM</b>Introduction to Ta Merosk</div><div class="num">26</div>
</section>

<section class="slide" style="left:258.9px;top:704px">
  <div class="card" style="left:14px;top:16px;width:199px;height:98px"></div>
  <table class="tbl" style="left:20px;top:22px;width:187px">
    <tr><th class="g">Project</th><th>20YY Plan</th><th>20YY Result</th><th>20YY Plan</th><th>20YY Result</th><th>20YY Plan</th><th>20YY Result</th><th class="g">Total Result</th></tr>
    <tr><td>Hurricane</td><td>12 670</td><td>12 450</td><td>12 670</td><td>12 450</td><td>12 670</td><td>12 450</td><td>37 350</td></tr>
    <tr><td>Rain</td><td>6 800</td><td>6800</td><td>6 800</td><td>6800</td><td>6 800</td><td>6800</td><td>20400</td></tr>
    <tr><td>Sunshine</td><td>9 300</td><td>10 400</td><td>9 300</td><td>10 400</td><td>9 300</td><td>10 400</td><td>31 200</td></tr>
    <tr><td>Lightning</td><td>13 450</td><td>13 450</td><td>13 450</td><td>13 450</td><td>13 450</td><td>13 450</td><td>40 350</td></tr>
    <tr><td>Flood</td><td>25 900</td><td>26 900</td><td>25 900</td><td>26 900</td><td>25 900</td><td>26 900</td><td>80 700</td></tr>
    <tr><td>Iceberg</td><td>130 800</td><td>130 700</td><td>130 800</td><td>130 700</td><td>130 800</td><td>130 700</td><td>392 100</td></tr>
    <tr><td>Tornado</td><td>19 800</td><td>19 150</td><td>19 800</td><td>19 150</td><td>19 800</td><td>19 150</td><td>57 450</td></tr>
    <tr><td>Fog</td><td>145 780</td><td>145 000</td><td>145 780</td><td>145 000</td><td>145 780</td><td>145 000</td><td>435 000</td></tr>
    <tr><td colspan="8" style="border:0;height:5px"></td></tr>
    <tr class="total"><td>Total</td><td style="background:var(--navy)">364 500</td><td style="background:var(--navy)">364850</td><td style="background:var(--navy)">364 500</td><td style="background:var(--navy)">364850</td><td style="background:var(--navy)">364 500</td><td style="background:var(--navy)">364850</td><td>1094050</td></tr>
  </table>
  <div class="foot"><b>TM</b>Introduction to Ta Merosk</div><div class="num">27</div>
</section>

<section class="slide" style="left:490.3px;top:704px">
  <div class="card" style="left:14px;top:16px;width:199px;height:98px"></div>
  <table class="tbl" style="left:20px;top:22px;width:187px">
    <tr><th class="g">Project</th><th>Q1</th><th>Q2</th><th>Q3</th><th>Q4</th></tr>
    <tr><td>Hurricane</td><td>12 670</td><td>12 450</td><td>12 670</td><td>12 450</td></tr>
    <tr><td>Rain</td><td>6 800</td><td>6800</td><td>6 800</td><td>6800</td></tr>
    <tr><td>Sunshine</td><td>9 300</td><td>10 400</td><td>9 300</td><td>10 400</td></tr>
    <tr><td>Lightning</td><td>13 450</td><td>13 450</td><td>13 450</td><td>13 450</td></tr>
    <tr><td>Flood</td><td>25 900</td><td>26 900</td><td>25 900</td><td>26 900</td></tr>
    <tr><td>Iceberg</td><td>130 800</td><td>130 700</td><td>130 800</td><td>130 700</td></tr>
    <tr><td>Tornado</td><td>19 800</td><td>19 150</td><td>19 800</td><td>19 150</td></tr>
    <tr><td>Fog</td><td>145 780</td><td>145 000</td><td>145 780</td><td>145 000</td></tr>
  </table>
  <div class="ab tiny" style="left:22px;top:87px;width:40px"><span style="color:var(--navy)">◎</span><br><b style="color:var(--ink)">Placeholder text</b><br>Lorem ipsum dolor sit amet</div>
  <div class="ab tiny" style="left:69px;top:87px;width:40px"><span style="color:var(--navy)">◎</span><br><b style="color:var(--ink)">Placeholder text</b><br>Lorem ipsum dolor sit amet</div>
  <div class="ab tiny" style="left:116px;top:87px;width:40px"><span style="color:var(--navy)">◎</span><br><b style="color:var(--ink)">Placeholder text</b><br>Lorem ipsum dolor sit amet</div>
  <div class="ab tiny" style="left:163px;top:87px;width:40px"><span style="color:var(--navy)">◎</span><br><b style="color:var(--ink)">Placeholder text</b><br>Lorem ipsum dolor sit amet</div>
  <div class="foot"><b>TM</b>Introduction to Ta Merosk</div><div class="num">28</div>
</section>

<section class="slide" style="left:721.7px;top:704px">
  <div class="card" style="left:14px;top:16px;width:199px;height:98px"></div>
  <table class="tbl" style="left:20px;top:22px;width:187px;font-size:1.8px">
    <tr><th class="g">Project</th><th>Jan</th><th>Feb</th><th>Mar</th><th>Apr</th><th>May</th><th>Jun</th><th>Jul</th><th>Aug</th><th>Sep</th><th>Oct</th><th>Nov</th><th>Dec</th></tr>
    <tr><td>Hurricane</td><td>12 670</td><td>12 450</td><td>12 670</td><td>12 450</td><td>12 670</td><td>12 450</td><td>12 670</td><td>12 450</td><td>12 670</td><td>12 450</td><td>12 670</td><td>12 450</td></tr>
    <tr><td>Rain</td><td>6 800</td><td>6800</td><td>6 800</td><td>6800</td><td>6 800</td><td>6800</td><td>6 800</td><td>6800</td><td>6 800</td><td>6800</td><td>6 800</td><td>6800</td></tr>
    <tr><td>Sunshine</td><td>9 300</td><td>10 400</td><td>9 300</td><td>10 400</td><td>9 300</td><td>10 400</td><td>9 300</td><td>10 400</td><td>9 300</td><td>10 400</td><td>9 300</td><td>10 400</td></tr>
    <tr><td>Lightning</td><td>13 450</td><td>13 450</td><td>13 450</td><td>13 450</td><td>13 450</td><td>13 450</td><td>13 450</td><td>13 450</td><td>13 450</td><td>13 450</td><td>13 450</td><td>13 450</td></tr>
    <tr><td>Flood</td><td>25 900</td><td>26 900</td><td>25 900</td><td>26 900</td><td>25 900</td><td>26 900</td><td>25 900</td><td>26 900</td><td>25 900</td><td>26 900</td><td>25 900</td><td>26 900</td></tr>
    <tr><td>Iceberg</td><td>130 800</td><td>130 700</td><td>130 800</td><td>130 700</td><td>130 800</td><td>130 700</td><td>130 800</td><td>130 700</td><td>130 800</td><td>130 700</td><td>130 800</td><td>130 700</td></tr>
    <tr><td>Tornado</td><td>19 800</td><td>19 150</td><td>19 800</td><td>19 150</td><td>19 800</td><td>19 150</td><td>19 800</td><td>19 150</td><td>19 800</td><td>19 150</td><td>19 800</td><td>19 150</td></tr>
    <tr><td>Fog</td><td>145 780</td><td>145 000</td><td>145 780</td><td>145 000</td><td>145 780</td><td>145 000</td><td>145 780</td><td>145 000</td><td>145 780</td><td>145 000</td><td>145 780</td><td>145 000</td></tr>
    <tr><td colspan="13" style="border:0;height:5px"></td></tr>
    <tr class="total"><td>Total</td><td style="background:var(--navy)">364 500</td><td style="background:var(--navy)">364850</td><td style="background:var(--navy)">364 500</td><td style="background:var(--navy)">364850</td><td style="background:var(--navy)">364 500</td><td style="background:var(--navy)">364850</td><td style="background:var(--navy)">364 500</td><td style="background:var(--navy)">364850</td><td style="background:var(--navy)">364 500</td><td style="background:var(--navy)">364850</td><td style="background:var(--navy)">364 500</td><td style="background:var(--navy)">364850</td></tr>
  </table>
  <div class="foot"><b>TM</b>Introduction to Ta Merosk</div><div class="num">29</div>
</section>

<section class="slide" style="left:953.7px;top:704px">
  <div class="card" style="left:14px;top:16px;width:199px;height:98px"></div>
  <table class="tbl" style="left:20px;top:22px;width:187px">
    <tr><th class="g">Project</th><th>20YY</th><th>20YY</th><th>20YY</th><th>20YY</th><th>20YY</th></tr>
    <tr><td>Hurricane</td><td>12 670</td><td>12 450</td><td>12 670</td><td>12 450</td><td>12 670</td></tr>
    <tr><td>Rain</td><td>6 800</td><td>6800</td><td>6 800</td><td>6800</td><td>6 800</td></tr>
    <tr><td>Sunshine</td><td>9 300</td><td>10 400</td><td>9 300</td><td>10 400</td><td>9 300</td></tr>
    <tr><td>Lightning</td><td>13 450</td><td>13 450</td><td>13 450</td><td>13 450</td><td>13 450</td></tr>
    <tr><td>Flood</td><td>25 900</td><td>26 900</td><td>25 900</td><td>26 900</td><td>25 900</td></tr>
    <tr><td>Iceberg</td><td>130 800</td><td>130 700</td><td>130 800</td><td>130 700</td><td>130 800</td></tr>
    <tr><td>Tornado</td><td>19 800</td><td>19 150</td><td>19 800</td><td>19 150</td><td>19 800</td></tr>
    <tr><td>Fog</td><td>145 780</td><td>145 000</td><td>145 780</td><td>145 000</td><td>145 780</td></tr>
    <tr class="navyrow"><td>Revenue</td><td>12 670</td><td>12 450</td><td>12 670</td><td>12 450</td><td>12 670</td></tr>
    <tr class="total"><td>Profit</td><td>6 800</td><td>6800</td><td>6 800</td><td>6800</td><td>6 800</td></tr>
    <tr class="navyrow"><td>Performance evaluation</td><td>A++</td><td>A</td><td>B-</td><td>B+</td><td>B++</td></tr>
  </table>
  <div class="foot"><b>TM</b>Introduction to Ta Merosk</div><div class="num">30</div>
</section>

<!-- Row 7 -->
<section class="slide" style="left:28.6px;top:838.9px">
  <div class="card" style="left:14px;top:14px;width:199px;height:98px"></div>
  <table class="tbl" style="left:20px;top:20px;width:90px">
    <tr><th colspan="2">Key indicators for 20YY</th></tr>
    <tr><td colspan="2" style="background:var(--gold);color:#fff">Main division</td></tr>
    <tr><td>Revenue</td><td>$ 118 000 000</td></tr><tr><td>Profit margin</td><td>$ 83 800 000</td></tr><tr><td>Staff full-time (employee)</td><td>100</td></tr><tr><td>Number of completed projects</td><td>83</td></tr><tr><td>International projects</td><td>63</td></tr><tr><td>Local projects</td><td>20</td></tr><tr><td>Result by year</td><td>102 %</td></tr>
    <tr><td colspan="2" style="border:0;height:3px"></td></tr>
    <tr><td colspan="2" style="background:var(--navy);color:#fff">Additional division</td></tr>
    <tr><td>Revenue</td><td>$ 118 000 000</td></tr><tr><td>Profit margin</td><td>$ 83 800 000</td></tr><tr><td>Staff full-time (employee)</td><td>100</td></tr><tr><td>Number of completed projects</td><td>83</td></tr><tr><td>Result by year</td><td>102 %</td></tr>
  </table>
  <table class="tbl" style="left:117px;top:20px;width:90px">
    <tr><th colspan="2">Key indicators for 20YY</th></tr>
    <tr><td colspan="2" style="background:var(--gold);color:#fff">Main division</td></tr>
    <tr><td>Revenue</td><td>$ 118 000 000</td></tr><tr><td>Profit margin</td><td>$ 83 800 000</td></tr><tr><td>Staff full-time (employee)</td><td>100</td></tr><tr><td>Number of completed projects</td><td>83</td></tr><tr><td>International projects</td><td>63</td></tr><tr><td>Local projects</td><td>20</td></tr><tr><td>Result by year</td><td>102 %</td></tr>
    <tr><td colspan="2" style="border:0;height:3px"></td></tr>
    <tr><td colspan="2" style="background:var(--navy);color:#fff">Additional division</td></tr>
    <tr><td>Revenue</td><td>$ 118 000 000</td></tr><tr><td>Profit margin</td><td>$ 83 800 000</td></tr><tr><td>Staff full-time (employee)</td><td>100</td></tr><tr><td>Number of completed projects</td><td>83</td></tr><tr><td>Result by year</td><td>102 %</td></tr>
  </table>
  <div class="foot"><b>TM</b>Introduction to Ta Merosk</div><div class="num">31</div>
</section>

<section class="slide" style="left:258.9px;top:838.9px">
  <div class="ab title" style="left:14px;top:22px;font-size:9px;font-weight:500;color:var(--navy)">Contact<br>Information</div>
  <div class="ab tiny" style="left:14px;top:48px;width:90px">Include your company name, address, phone number and email address as basic contact details. Add social links, a feedback form and business hours so customers can reach you with ease.</div>
  <div class="card" style="left:14px;top:76px;width:27px;height:30px"><div class="tiny" style="padding:3px"><b style="color:var(--ink)">Paris</b><br>14 Rue Sellin, 75011 Paris, France</div></div>
  <div class="card" style="left:45px;top:76px;width:27px;height:30px"><div class="tiny" style="padding:3px"><b style="color:var(--ink)">Berlin</b><br>Lindenweg 42, 10115 Berlin, Germany</div></div>
  <div class="card" style="left:76px;top:76px;width:27px;height:30px"><div class="tiny" style="padding:3px"><b style="color:var(--ink)">Los Angeles</b><br>512 Harbor Ave, Los Angeles, CA 90012</div></div>
  <div class="photo photo-city" role="img" aria-label="City skyline across a calm waterfront" style="left:125px;top:16px;width:88px;height:92px"></div>
  <div class="num">32</div>
</section>

</main>
</body>
</html>
```